Business Card for TOV

We need a Corporate style business card for a new Industrial recycling company based in Australia. We recycle industrial products from Mining companies, power stations and other large industry all around the country.

We want the card to represent a modern, innovative professional company that is an industry leader.

We want the card to be double sided. I think with the logo centred by itself on one side and the text displayed with all our details on the other side.

(or you could put the persons name with the job title on the side with the logo?? I'll leave that up to your creative sides)

Open to how you divide and place the information on the one side of the card.

I think the persons name and the title should have its own place. The rest of the information can be placed as you think is best and then I will provide feedback as to what I think works best.

I have attached the logo file so you can add that to the one side. Whether you use it in a smaller form on the second side too is an option but I'll leave that up to you initially?

Information required on the card is as follows

Dermot Halloran
Director

0438 972 506

dermot@tovq.com.au

Po Box 782
Brindle ACT 2694

www.tovq.com.au

ACN 582 917 306 (This can be in very small print and can be in the bottom corner of the card or somewhere not very prominent

Wanted to thank everyone for their submissions. 

We were really torn on about 5 designs in the end.

We decided to go with the first one we liked.

We have another company that is going to need logo and business card design in the coming weeks.

I will save your designer ID's so I can invite you all to that project. too!

Thanks again and all the best

Dermot

Target Market(s)

Corporate and medium to large business clients

Industry/Entity Type

Industrial

```html
<!DOCTYPE html>
<html lang="en">
<head>
<meta charset="utf-8">
<title>TOV Resource Group – Business Card</title>
<link rel="stylesheet" href="https://fonts.googleapis.com/css2?family=Gelasio:wght@700&display=swap">
<style>
  :root {
    --stage: #555354;
    --card: #ffffff;
    --label: #f6e6e6;
    --ink: #333333;
    --blue: #2a8ab8;
    --green: #8dc63f;
    --black: #333333;
    --red: #d92027;
    --serif: "Gelasio", Georgia, serif;
  }
  html, body {
    margin: 0;
    padding: 0;
    width: 1200px;
    height: 900px;
    overflow: hidden;
    background: var(--stage);
  }
  .canvas {
    position: relative;
    width: 1200px;
    height: 900px;
    font-family: var(--serif);
  }
  .side-label {
    position: absolute;
    margin: 0;
    color: var(--label);
    font-weight: 700;
    font-size: 48px;
    line-height: 1;
  }
  .side-label--back { left: 122px; top: 170px; }
  .side-label--front { left: 126px; top: 600px; }

  .card {
    position: absolute;
    left: 474px;
    width: 673px;
    height: 391px;
    background: var(--card);
    overflow: hidden;
  }
  .card--back { top: 34px; }
  .card--front { top: 480px; }

  .stripe {
    position: absolute;
    top: 0;
    bottom: 0;
    width: 12px;
  }
  .stripe--blue  { left: 545px; background: var(--blue); }
  .stripe--green { left: 584px; background: var(--green); }
  .stripe--black { left: 623px; background: var(--black); }
  .stripe--red   { left: 662px; width: 11px; background: var(--red); }

  .brand {
    position: absolute;
    display: flex;
    align-items: center;
    gap: 24px;
  }
  .card--back .brand { left: 10px; top: 130px; }
  .card--front .brand { left: 14px; top: 40px; }
  .brand__mark {
    width: 124px;
    height: 124px;
    border-radius: 50%;
    background: var(--green);
    flex: none;
  }
  .brand__name {
    margin: 0;
    color: var(--ink);
    font-weight: 700;
    font-size: 32px;
    line-height: 36px;
    letter-spacing: 2px;
    white-space: nowrap;
  }
  .brand__line { display: block; }

  .divider {
    position: absolute;
    left: 0;
    top: 197px;
    width: 545px;
    height: 3px;
    background: var(--blue);
  }

  .contact {
    position: absolute;
    left: 25px;
    top: 226px;
    margin: 0;
    padding: 0;
    list-style: none;
    font-weight: 700;
    font-size: 19px;
  }
  .contact__item { height: 34px; line-height: 26px; white-space: nowrap; }
  .contact__item--phone { color: var(--ink); }
  .contact__item--post  { color: var(--green); }
  .contact__item--email { color: var(--blue); }
  .contact__item--web   { color: var(--red); }

  .person {
    position: absolute;
    right: 155px;
    top: 226px;
    margin: 0;
    text-align: right;
    color: var(--ink);
    font-weight: 700;
  }
  .person__name { display: block; font-size: 19px; line-height: 26px; }
  .person__title { display: block; font-size: 15px; line-height: 24px; color: var(--blue); }

  .company-number {
    position: absolute;
    right: 155px;
    bottom: 20px;
    margin: 0;
    color: var(--ink);
    font-weight: 700;
    font-size: 10px;
    line-height: 12px;
  }
</style>
</head>
<body>
<main class="canvas">
  <p class="side-label side-label--back">back</p>
  <section class="card card--back" aria-label="Card back">
    <div class="brand">
      <span class="brand__mark" aria-hidden="true"></span>
      <p class="brand__name"><span class="brand__line">TOV</span><span class="brand__line">RESOURCE GROUP</span></p>
    </div>
    <span class="stripe stripe--blue"></span>
    <span class="stripe stripe--green"></span>
    <span class="stripe stripe--black"></span>
    <span class="stripe stripe--red"></span>
  </section>

  <p class="side-label side-label--front">front</p>
  <section class="card card--front" aria-label="Card front">
    <div class="brand">
      <span class="brand__mark" aria-hidden="true"></span>
      <p class="brand__name"><span class="brand__line">TOV</span><span class="brand__line">RESOURCE GROUP</span></p>
    </div>
    <span class="divider"></span>
    <ul class="contact">
      <li class="contact__item contact__item--phone">Phone: 0438 972 506</li>
      <li class="contact__item contact__item--post">PO Box: 782 Brindle ACT 2694</li>
      <li class="contact__item contact__item--email">Email: dermot@tovq.com.au</li>
      <li class="contact__item contact__item--web">Web: www.tovq.com.au</li>
    </ul>
    <p class="person">
      <span class="person__name">Dermot Halloran</span>
      <span class="person__title">Director</span>
    </p>
    <p class="company-number">ACN 582 917 306</p>
    <span class="stripe stripe--blue"></span>
    <span class="stripe stripe--green"></span>
    <span class="stripe stripe--black"></span>
    <span class="stripe stripe--red"></span>
  </section>
</main>
</body>
</html>
```